Business Card Design

We need a business card design for a Non-Profit Christian Based Organization located in Milford, Pa.
Alder Ridge Open Door Relief
Is a Christ-centered organization dedicated to providing compassion and hope to homeless or near homeless, families and individuals, by meeting their basic and urgent need of food, clothing and shelter.
Updates
the logo is black and white
and must add the color green some where 00400
Industry/Entity Type
Clothing
Contact Information for Business Card
Alder Ridge Open Door Relief
P.O. Box 817
Elmbrook, Pa 18452
Phone: (570) 384-CARE(2273)
Toll Free: (855) 384-CARE
email:Info@alderridgeodr.org
email:Careline@alderridgeodr.org
Our organization already has a logo.
Front of card:
Is a Christ-centered organization dedicated to providing compassion and hope to homeless or near homes, families and individual by meeting their basic and urgent need of food, clothing and shelter.(this is our Mission Statement)
On back of card:
'I was hungry and you gave me something to eat;
"I was thirsty and you gave me something to drink;
"I was a stranger and you invited me in."
Matthew 25:35
Color: Logo is black and white
Background color I would like a bright light green 00ff00(close to that)
I attached a sample of what I created on Quill Press but, I don't like the color green, nor the design (but I just wanted to give you and Idea of the Logo and Alder Ridge (one line) Open Door Relief (second line) in a different font thank you
Colette Marsh
Pr/Board of Directors

```html
<!DOCTYPE html>
<html lang="en">
<head>
<meta charset="utf-8">
<title>Alder Ridge Open Door Relief — Business Card</title>
<link rel="stylesheet" href="https://fonts.googleapis.com/css2?family=Open+Sans:ital,wght@0,400;0,600;0,700;1,400&display=swap">
<style>
  :root {
    --canvas: #e9e9e7;
    --card: #ffffff;
    --ink: #1a1a1a;
    --ink-soft: #2e2e2e;
    --green: #8cc63f;
    --green-light: #c5e59a;
    --shadow: rgba(0, 0, 0, 0.18);
  }
  * { box-sizing: border-box; margin: 0; padding: 0; }
  html, body {
    width: 1200px; height: 1200px; overflow: hidden;
    background: var(--canvas);
    font-family: "Open Sans", Arial, sans-serif;
    color: var(--ink);
  }
  .sheet {
    width: 1200px; height: 1200px;
    display: flex; flex-direction: column; align-items: center; justify-content: center;
    gap: 70px;
  }
  .card {
    position: relative;
    width: 860px; height: 491px;
    background: var(--card);
    box-shadow: 0 6px 22px var(--shadow);
  }
  .rule {
    position: absolute;
    height: 9px;
    border-top: 3px solid var(--green);
    border-bottom: 3px solid var(--green-light);
  }
  .brand {
    position: absolute;
    display: flex; flex-direction: column;
    font-weight: 600; color: var(--ink);
    text-transform: uppercase; line-height: 1.15;
  }
  .brand-mark { background: var(--ink); }

  /* Contact side */
  .card--contact .brand { left: 44px; top: 84px; font-size: 16px; align-items: center; text-align: center; }
  .card--contact .brand-mark { width: 58px; height: 58px; margin-bottom: 14px; }
  .contact-list {
    position: absolute; left: 228px; top: 40px;
    list-style: none; font-size: 17.5px; line-height: 27px; color: var(--ink-soft);
  }
  .card--contact .rule { left: 60px; right: 56px; top: 240px; }
  .verse {
    position: absolute; right: 56px; top: 276px;
    text-align: right; font-size: 27px; line-height: 38px; color: var(--ink);
  }
  .verse-ref { display: block; margin-top: 6px; font-size: 15px; font-style: italic; line-height: 20px; }

  /* Mission side */
  .card--mission .brand { left: 66px; top: 56px; font-size: 26px; }
  .card--mission .brand-mark { width: 92px; height: 92px; margin: 0 0 22px 44px; }
  .card--mission .rule { left: 66px; right: 60px; top: 288px; }
  .mission {
    position: absolute; left: 66px; right: 60px; top: 312px;
    font-size: 18px; line-height: 27px; color: var(--ink);
  }
</style>
</head>
<body>
<main class="sheet">
  <section class="card card--contact" aria-label="Card side with contact details">
    <div class="brand">
      <span class="brand-mark" aria-hidden="true"></span>
      <span>Alder Ridge</span>
      <span>Open Door Relief</span>
    </div>
    <ul class="contact-list">
      <li>P.O. Box 817 Elmbrook</li>
      <li>Pa 18452</li>
      <li>Phone: (570) 384-CARE(2273)</li>
      <li>Toll Free: (855) 384-CARE</li>
      <li>email:Info@alderridgeodr.org</li>
      <li>email:Careline@alderridgeodr.org</li>
    </ul>
    <div class="rule" aria-hidden="true"></div>
    <p class="verse">
      'I was hungry and you gave me something to eat;<br>
      "I was thirsty and you gave me something to drink;<br>
      "I was a stranger and you invited me in."
      <span class="verse-ref">-Matthew 25:35-</span>
    </p>
  </section>

  <section class="card card--mission" aria-label="Card side with mission statement">
    <div class="brand">
      <span class="brand-mark" aria-hidden="true"></span>
      <span>Alder Ridge</span>
      <span>Open Door Relief</span>
    </div>
    <div class="rule" aria-hidden="true"></div>
    <p class="mission">Christ-centered organization dedicated to providing compassion and hope to homeless or near homes, families and individual by meeting their basic and urgent need of food, clothing and shelter</p>
  </section>
</main>
</body>
</html>
```